New Wordpress Website

We need a new wordpress website for our IT Association. Our main corporate colour is orange. Style Guideline attached.
The association is an NFP for IT Professionals. An opportunity for our members to collaborate and grow as a community.

Current website can be found at: www.crestlanetechguild.org

Target Market(s)

IT Professionals and Small Business Owners who need IT Information

Industry/Entity Type

Information Technology

Coding

Coded - Design and coding required

Colors
f37122

```html
<!DOCTYPE html>
<html lang="en">
<head>
<meta charset="utf-8">
<title>Crestlane Tech Guild</title>
<link href="https://fonts.googleapis.com/css2?family=Barlow:wght@400;500;600;700;800&family=Roboto:wght@400;500;700&display=swap" rel="stylesheet">
<style>
:root{
  --orange:#f37122;
  --orange-dark:#e0641a;
  --ink:#1d1d1f;
  --dark:#1a1a1a;
  --grey:#e9e9ea;
  --nav:#dcdcdc;
  --text:#333;
  --muted:#777;
  --white:#fff;
}
*{box-sizing:border-box;margin:0;padding:0}
html,body{width:1200px;height:4702px;overflow:hidden}
body{position:relative;font-family:"Roboto",sans-serif;color:var(--text);background:var(--white)}
.abs{position:absolute}
h1,h2,h3,.head{font-family:"Barlow",sans-serif}

/* header */
.site-header{left:0;top:0;width:1200px;height:146px;background:var(--white)}
.brand{left:142px;top:26px;display:flex;align-items:center;gap:14px}
.brand-mark{width:86px;height:86px;border-radius:50%;border:9px solid var(--orange)}
.brand-name{font-family:"Barlow",sans-serif;font-weight:700;color:var(--ink);font-size:30px;line-height:1.05;letter-spacing:1px}
.contact-box{left:464px;top:0;width:579px;height:104px;background:var(--orange);color:var(--white)}
.phone-badge{left:40px;top:26px;width:52px;height:52px;border-radius:50%;background:var(--dark);display:flex;align-items:center;justify-content:center}
.call{left:116px;top:24px;font-size:17px}
.call b{display:block;font-size:25px;font-weight:700;margin-top:2px}
.follow{left:370px;top:22px;font-size:17px}
.socials{display:flex;gap:12px;margin-top:14px}
.socials span{width:26px;height:26px;border:2px solid var(--white);border-radius:50%;display:block}
.main-nav{left:0;top:146px;width:1200px;height:50px;background:var(--nav);display:flex;align-items:center;padding-left:142px}
.main-nav a{font-size:13px;color:var(--ink);text-decoration:none;margin-right:48px;letter-spacing:.3px}
.main-nav a.active{color:var(--orange)}

/* hero */
.hero{left:0;top:196px;width:1200px;height:616px;background:radial-gradient(ellipse at 70% 40%,#3a3a3a,#141414 70%)}
.hero-art{left:620px;top:70px;width:440px;height:460px;border-radius:50%;background:radial-gradient(circle,#6f7b88 0%,#3b4450 55%,#2a2a2a 72%,transparent 73%)}
.hero h1{left:142px;top:140px;font-size:88px;line-height:.95;font-weight:700}
.hero h1 .o{color:var(--orange)}
.hero h1 .w{color:var(--white)}
.hero-sub{left:144px;top:322px;color:var(--white);font-size:23px;font-family:"Barlow",sans-serif}
.btn{display:inline-flex;align-items:center;gap:10px;font-family:"Barlow",sans-serif;font-weight:500;text-decoration:none}
.btn-orange{background:var(--orange);color:var(--white)}
.btn-white{background:var(--white);color:var(--ink)}
.hero .b1{left:144px;top:372px;height:50px;padding:0 26px;font-size:16px}
.hero .b2{left:423px;top:372px;height:50px;padding:0 22px;font-size:16px}
.dots{left:145px;top:460px;display:flex;gap:6px}
.dots i{width:8px;height:8px;border-radius:50%;border:1.5px solid var(--white);display:block}
.dots i.on{background:var(--orange);border-color:var(--orange)}
.hero-edge{left:0;top:800px;width:1200px;height:44px}

/* about */
.about{left:0;top:840px;width:1200px;height:950px;background:linear-gradient(180deg,#ececec,#e4e4e5)}
.about-frame{left:142px;top:62px;width:226px;height:330px;background:var(--orange)}
.about-photo{left:156px;top:75px;width:322px;height:386px;background:linear-gradient(135deg,#8d8f93,#4b4f57);box-shadow:0 10px 25px rgba(0,0,0,.25)}
.about-photo2{left:397px;top:204px;width:162px;height:172px;border:4px solid var(--white);background:linear-gradient(135deg,#5a6270,#2f343c)}
.sec-mark{width:28px;height:28px;border-radius:50%;border:4px solid var(--orange)}
.about .sec-mark{left:682px;top:90px}
.about h2{left:594px;top:130px;font-size:42px;font-weight:700;color:var(--ink)}
.about h2 span{color:var(--orange)}
.about .lead{left:594px;top:196px;width:454px;font-family:"Barlow",sans-serif;font-weight:600;font-size:18px;line-height:1.2;color:var(--ink)}
.about .body{left:594px;top:256px;width:450px;font-size:11px;line-height:1.6;text-align:justify;color:#444}
.about .more{left:594px;top:388px;height:38px;padding:0 16px;font-size:15px}
.feature{width:300px}
.ring{width:188px;height:188px;border-radius:50%;background:var(--white);box-shadow:0 6px 18px rgba(0,0,0,.12);display:flex;align-items:center;justify-content:center}
.ring .inner{width:150px;height:150px;border-radius:50%;border:1px dashed #d8b7a4;display:flex;align-items:center;justify-content:center;background:#fbfbfb}
.feature h3{margin:52px 0 0 46px;font-size:32px;font-weight:600;color:var(--ink)}
.feature p{margin:6px 0 0 46px;width:240px;font-size:11px;line-height:1.45;color:#333}
.feature .tiny{margin:14px 0 0 46px;height:17px;padding:0 8px;font-size:7px;display:inline-flex}

/* video */
.video-sec{left:0;top:1790px;width:1200px;height:657px;background:var(--white)}
.laptop{left:237px;top:92px;width:703px;height:470px;background:#2b2b2d;border-radius:14px}
.screen{left:34px;top:34px;width:635px;height:398px;background:linear-gradient(160deg,#6d6258,#2f2a26)}
.vid-title{left:44px;top:14px;color:var(--white);font-size:14px}
.play{left:286px;top:164px;width:64px;height:64px;border-radius:50%;background:rgba(0,0,0,.45);border:3px solid var(--white);display:flex;align-items:center;justify-content:center}
.bar{left:10px;top:362px;width:615px;height:3px;background:rgba(255,255,255,.4)}
.laptop-base{left:127px;top:561px;width:923px;height:16px;border-radius:0 0 40px 40px;background:linear-gradient(#3a3a3c,#1c1c1d);box-shadow:0 18px 22px rgba(0,0,0,.15)}

/* testimonials */
.testi{left:0;top:2447px;width:1200px;height:626px;background:var(--orange)}
.testi .sec-mark{left:586px;top:82px;border-color:var(--white)}
.testi h2{left:0;top:124px;width:1200px;text-align:center;font-size:44px;font-weight:700;color:var(--ink)}
.testi h2 span{color:var(--white)}
.card{top:213px;width:409px;height:256px;background:var(--white);border-radius:18px;box-shadow:0 8px 20px rgba(0,0,0,.15)}
.avatar{left:28px;top:32px;width:104px;height:104px;border-radius:50%;border:2px solid #ddd;background:linear-gradient(#cfd3d8,#8d949c)}
.quote{right:30px;top:22px;font-family:"Barlow",sans-serif;font-size:200px;line-height:1;color:#ececec;font-weight:800}
.who{left:150px;width:230px;font-size:10px;line-height:1.7;color:var(--orange);text-transform:uppercase}
.said{left:26px;top:150px;width:357px;text-align:center;font-size:11px;line-height:1.65;color:#555}
.t-dots{left:551px;top:534px;display:flex;gap:15px}
.t-dots i{width:20px;height:20px;border-radius:50%;border:2px solid var(--white);display:block}
.t-dots i.on{background:var(--white)}

/* chapter */
.chapter{left:0;top:3073px;width:1200px;height:460px;background:radial-gradient(ellipse at center,#2a2a2a,#121212 75%)}
.flask{left:76px;top:120px;width:176px;height:190px;border-radius:50%;background:radial-gradient(circle at 45% 55%,#bcbcbc,#6a6a6a 65%,transparent 67%)}
.figure{left:895px;top:130px;width:280px;height:330px;background:linear-gradient(180deg,#e9e9e9,#9d9d9d);border-radius:40% 40% 10% 10%}
.chapter .l1{left:416px;top:70px;font-family:"Barlow",sans-serif;font-size:54px;color:var(--orange)}
.chapter .l2{left:412px;top:160px;font-family:"Barlow",sans-serif;font-weight:800;font-size:80px;line-height:1;color:var(--white)}
.chapter .l3{left:412px;top:258px;font-family:"Barlow",sans-serif;font-size:46px;color:var(--white)}
.chapter .l4{left:410px;top:316px;font-family:"Barlow",sans-serif;font-size:54px;color:var(--orange)}
.find{left:622px;top:335px;height:42px;padding:0 14px;border:1.5px solid var(--white);color:var(--white);font-size:16px}

/* partners */
.partners{left:0;top:3533px;width:1200px;height:384px;background:var(--white)}
.side-tab{left:0;top:20px;width:48px;height:120px;background:var(--white);box-shadow:0 2px 8px rgba(0,0,0,.15)}
.side-tab i{display:block;width:18px;height:18px;margin:12px auto;border-radius:50%;border:2px solid #bbb}
.side-tab i.o{background:var(--orange);border-color:var(--orange)}
.tab-label{left:64px;top:22px;padding:8px 16px;font-size:12px;color:#444;background:var(--white);box-shadow:0 2px 6px rgba(0,0,0,.15)}
.partners .sec-mark{left:586px;top:82px}
.partners h2{left:0;top:122px;width:1200px;text-align:center;font-size:44px;font-weight:700;color:var(--orange)}
.partners h2 span{color:var(--ink)}
.logo-band{left:0;top:237px;width:1200px;height:100px;background:#f4f4f4;display:flex;align-items:center;justify-content:space-around;padding:0 20px}
.logo-band span{font-family:"Barlow",sans-serif;font-weight:500;font-size:36px;color:#a8a8a8}
.footer-edge{left:0;top:3985px;width:1200px;height:40px}

/* newsletter + footer */
.footer{left:0;top:4017px;width:1200px;height:685px;background:#111}
.nl-title{left:0;top:68px;width:1200px;text-align:center;font-family:"Barlow",sans-serif;font-size:25px;color:var(--white)}
.nl-title span{color:var(--orange)}
.nl-sub{left:0;top:108px;width:1200px;text-align:center;font-size:10px;color:#ccc}
.nl-form{left:274px;top:155px;width:652px;height:73px;background:#1d1d1d;display:flex;align-items:center;justify-content:space-between;padding:0 24px 0 30px}
.nl-form span{font-size:11px;color:#666}
.nl-form b{background:var(--orange);color:var(--white);font-size:10px;font-weight:700;padding:11px 16px}
.f-brand{left:142px;top:340px;display:flex;align-items:center;gap:12px}
.f-brand .brand-mark{width:68px;height:68px;border-width:7px}
.f-brand .brand-name{color:var(--white);font-size:25px}
.f-about{left:144px;top:430px;width:250px;font-size:11px;line-height:1.6;color:#ddd}
.f-col h3{font-size:25px;font-weight:600;color:var(--white)}
.f-links{display:grid;grid-template-columns:172px 120px;row-gap:12px;margin-top:30px}
.f-links a{font-size:12px;color:var(--white);text-decoration:none;display:flex;align-items:center;gap:10px}
.f-links a::before{content:"";width:9px;height:9px;border-radius:50%;border:2px solid var(--orange)}
.f-contact li{list-style:none;display:flex;align-items:center;gap:14px;font-size:12px;color:var(--white);margin-top:26px}
.f-soc{display:flex;gap:10px;margin-top:24px}
.f-soc span{width:26px;height:26px;border-radius:50%;background:var(--white);display:block}
.copy{left:0;top:620px;width:1200px;text-align:center;font-size:11px;color:#ddd}
.keyp{left:0;top:651px;width:1200px;text-align:center;font-size:8px;color:#ccc}
.keyp b{font-size:11px;margin-left:6px;color:var(--white)}
</style>
</head>
<body>

<header class="abs site-header">
  <div class="abs brand">
    <span class="brand-mark"></span>
    <div class="brand-name">CRESTLANE<br>TECH GUILD</div>
  </div>
  <div class="abs contact-box">
    <div class="abs phone-badge">
      <svg width="22" height="30" viewBox="0 0 22 30"><rect x="2" y="1" width="18" height="28" rx="3" fill="none" stroke="#fff" stroke-width="2.5"/><circle cx="11" cy="24" r="1.8" fill="#fff"/></svg>
    </div>
    <div class="abs call">Call Us On:<b>1300 555 017</b></div>
    <div class="abs follow">Follow Us On:
      <div class="socials"><span></span><span></span><span></span><span></span></div>
    </div>
  </div>
</header>

<nav class="abs main-nav">
  <a class="active" href="#">HOW IT WORKS</a><a href="#">JOIN</a><a href="#">CHAPTERS</a><a href="#">MEMBERS</a><a href="#">PARTNERS</a><a href="#">MEDIA</a><a href="#">EVENTS</a><a href="#">SHOP</a><a href="#">ABOUT US</a>
</nav>

<section class="abs hero">
  <div class="abs hero-art" role="img" aria-label="Businesswoman viewing a wall of data screens inside a circular network graphic"></div>
  <h1 class="abs"><span class="o">STRENGTH</span><br><span class="w">IN NUMBERS</span></h1>
  <p class="abs hero-sub">Grow your business, Grow your reputation.</p>
  <a class="abs btn btn-orange b1" href="#">DOWNLOAD BROCHURE
    <svg width="22" height="18" viewBox="0 0 22 18"><path d="M6 14H5a4 4 0 0 1 0-8 6 6 0 0 1 11.5 1A3.5 3.5 0 0 1 17 14h-1M11 8v8m-3-3 3 3 3-3" fill="none" stroke="#fff" stroke-width="1.6"/></svg></a>
  <a class="abs btn btn-white b2" href="#">JOIN US
    <svg width="18" height="12" viewBox="0 0 18 12"><path d="M2 1l5 5-5 5M9 1l5 5-5 5" fill="none" stroke="#1d1d1f" stroke-width="2"/></svg></a>
  <div class="abs dots"><i class="on"></i><i></i><i></i></div>
</section>
<svg class="abs hero-edge" viewBox="0 0 1200 44" preserveAspectRatio="none"><polygon points="0,12 1200,0 1200,20 0,32" fill="#f37122"/></svg>

<section class="abs about">
  <div class="abs about-frame"></div>
  <div class="abs about-photo" role="img" aria-label="Team of IT professionals gathered around a computer screen"></div>
  <div class="abs about-photo2" role="img" aria-label="Developer working at a laptop"></div>
  <span class="abs sec-mark"></span>
  <h2 class="abs"><span>ABOUT</span> US</h2>
  <p class="abs lead">Crestlane Tech Guild is a not-for-profit Association; founded in Australia in 2011.</p>
  <p class="abs body">Uniquely positioned as a conduit for individual IT business owners and professionals, IT service providers and IT vendors to collaborate on solutions specific to the needs of small and medium business, Crestlane Tech Guild has grown rapidly and now represents 300+ members across Australia. Crestlane Tech Guild is governed by a Board of Directors and supported by a National Executive Committee as below:</p>
  <a class="abs btn btn-orange more" href="#">VIEW MORE
    <svg width="16" height="12" viewBox="0 0 18 12"><path d="M2 1l5 5-5 5M9 1l5 5-5 5" fill="none" stroke="#fff" stroke-width="2"/></svg></a>

  <div class="abs feature" style="left:142px;top:526px">
    <div class="ring"><div class="inner">
      <svg width="60" height="70" viewBox="0 0 60 70"><circle cx="30" cy="28" r="16" fill="#f37122"/><rect x="23" y="46" width="14" height="12" fill="#f37122"/><path d="M30 2v6M8 10l4 4M52 10l-4 4M2 28h6M52 28h6" stroke="#f37122" stroke-width="3"/></svg>
    </div></div>
    <h3 class="head">SEEK</h3>
    <p>Liberate your time and find proven IT solutions fast via the Crestlane Tech Guild Forum.</p>
    <a class="btn btn-orange tiny" href="#">VIEW MORE »</a>
  </div>
  <div class="abs feature" style="left:460px;top:526px">
    <div class="ring"><div class="inner">
      <svg width="72" height="64" viewBox="0 0 72 64"><rect x="2" y="2" width="68" height="60" rx="6" fill="#f37122"/><rect x="8" y="8" width="56" height="4" fill="#fff"/><path d="M22 48l14-24 14 24zM30 42l5 4 8-10" fill="none" stroke="#fff" stroke-width="3"/></svg>
    </div></div>
    <h3 class="head">SOLVE</h3>
    <p>Create a more efficient and effective business, and deliver greater value to your customers via fast, effective problem-solving.</p>
    <a class="btn btn-orange tiny" href="#">VIEW MORE »</a>
  </div>
  <div class="abs feature" style="left:758px;top:526px">
    <div class="ring"><div class="inner">
      <svg width="70" height="60" viewBox="0 0 70 60"><path d="M4 56C6 30 22 20 42 20V4l24 24-24 24V36C26 36 14 42 4 56z" fill="#f37122"/></svg>
    </div></div>
    <h3 class="head">SHARE</h3>
    <p>Join the collective buying power and influence of Australia's largest industry association for small and medium business IT.</p>
    <a class="btn btn-orange tiny" href="#">VIEW MORE »</a>
  </div>
</section>

<section class="abs video-sec">
  <div class="abs laptop">
    <div class="abs screen" role="img" aria-label="Video still of members seated at a boardroom meeting">
      <div class="abs vid-title">Crestlane Tech Guild - There's strength in numbers</div>
      <div class="abs play"><svg width="22" height="24" viewBox="0 0 22 24"><polygon points="5,3 20,12 5,21" fill="#fff"/></svg></div>
      <div class="abs bar"></div>
    </div>
  </div>
  <div class="abs laptop-base"></div>
</section>

<section class="abs testi">
  <span class="abs sec-mark"></span>
  <h2 class="abs">OUR <span>TESTIMONIALS</span></h2>
  <article class="abs card" style="left:175px">
    <div class="abs quote">”</div>
    <div class="abs avatar" role="img" aria-label="Portrait of the reviewer"></div>
    <div class="abs who" style="top:78px">Daniel Mercer, Director<br>Northfield Advisory Group Pty Ltd<br>Crestlane Tech Guild, Melbourne</div>
    <p class="abs said">Our business has grown thanks to Crestlane Tech Guild and has connected us to new business opportunities, created additional revenue and we have completed successful mergers and acquisitions with three other Crestlane Tech Guild Members.</p>
  </article>
  <article class="abs card" style="left:604px">
    <div class="abs quote">”</div>
    <div class="abs avatar" role="img" aria-label="Portrait of the reviewer"></div>
    <div class="abs who" style="top:90px">Owen Hartley – National Sales Manager<br>Kestrel Systems Australia Limited</div>
    <p class="abs said" style="text-align:justify">Our partnership with Crestlane Tech Guild has helped Kestrel better understand the needs of the SMB IT market and to showcase our solutions to technical experts in a meaningful and engaging way.</p>
  </article>
  <div class="abs t-dots"><i></i><i class="on"></i><i></i></div>
</section>

<section class="abs chapter">
  <div class="abs flask" role="img" aria-label="Glass flask illustration"></div>
  <div class="abs figure" role="img" aria-label="3D figure searching with a magnifying glass beside a red question mark"></div>
  <div class="abs l1">Find your local</div>
  <div class="abs l2">CRESTLANE</div>
  <div class="abs l3">TECH GUILD</div>
  <div class="abs l4">Chapter.</div>
  <a class="abs btn find" href="#">FIND NOW
    <svg width="18" height="18" viewBox="0 0 18 18"><circle cx="7.5" cy="7.5" r="5.5" fill="none" stroke="#fff" stroke-width="2"/><path d="M12 12l5 5" stroke="#fff" stroke-width="2"/></svg></a>
</section>

<section class="abs partners">
  <div class="abs side-tab"><i class="o"></i><i></i><i></i></div>
  <div class="abs tab-label">Becoming a Partner</div>
  <span class="abs sec-mark"></span>
  <h2 class="abs">OUR <span>PARTNERS</span></h2>
  <div class="abs logo-band">
    <span>Bytevale</span><span>QuickSpark Tools</span><span>Wardline</span><span>Corvex</span><span>VaultNest</span>
  </div>
</section>
<svg class="abs footer-edge" viewBox="0 0 1200 40" preserveAspectRatio="none"><polygon points="0,10 1200,22 1200,40 0,40" fill="#f37122"/></svg>

<footer class="abs footer">
  <div class="abs nl-title"><span>SUBSCRIBE</span> TO OUR NEWSLETTER</div>
  <div class="abs nl-sub">SEND US A NEWSLETTER TO GET UPDATE.</div>
  <div class="abs nl-form"><span>Your E-Mail Address</span><b>SUBSCRIBE NOW</b></div>

  <div class="abs f-brand"><span class="brand-mark"></span><div class="brand-name">CRESTLANE<br>TECH GUILD</div></div>
  <p class="abs f-about">Crestlane Tech Guild is Australia's leading industry association for IT business owners and professionals specialising in IT solutions for small and medium business.</p>

  <div class="abs f-col" style="left:498px;top:342px">
    <h3 class="head">QUICK LINKS</h3>
    <div class="f-links">
      <a href="#">HOW IT WORKS</a><a href="#">MEDIA</a>
      <a href="#">JOIN</a><a href="#">EVENTS</a>
      <a href="#">CHAPTERS</a><a href="#">SHOP</a>
      <a href="#">MEMBERS</a><a href="#">ABOUT US</a>
      <a href="#">PARTNERS</a>
    </div>
  </div>
  <div class="abs f-col" style="left:882px;top:342px">
    <h3 class="head">CONTACT US</h3>
    <ul class="f-contact">
      <li><svg width="16" height="16" viewBox="0 0 16 16"><path d="M3 1l3 3-1.5 2a9 9 0 0 0 5.5 5.5L12 10l3 3-2 2C7 15 1 9 1 3z" fill="#f37122"/></svg>1300 555 017</li>
      <li><svg width="16" height="16" viewBox="0 0 16 16"><polygon points="1,7 15,1 9,15 7,9" fill="#f37122"/></svg>hello@crestlaneguild.org</li>
    </ul>
    <div class="f-soc"><span></span><span></span><span></span><span></span></div>
  </div>

  <div class="abs copy">© Copyright 2020. All rights reserved. Crestlane Tech Guild Limited.</div>
  <div class="abs keyp">KEY PARTNER <b>KEYSTONE GRID</b></div>
</footer>

</body>
</html>
```